Holistic Therapy (aromatherapy, massage, reflexology, life coaching, soul healing, aura reading)

I work for myself as a holistic therapist doing: aromatherapy massage, massage, reflexology, abdominal-sacral massage, life coaching, soul healing, aura readings. I want a business card that doesn't focus on any one of these( so not just feet or a massage couch,but rather a card that creates the feeling of wholeness, healing, health and which can encompass all my therapies - e.g. green or purple are colours I like (especially green, or maybe green on back and purple on front). It's going to be called Rosa Pell Therapies. I don't want to list all my therapies on the card in case I add others later.). At some point I will create a website but in this instance I just want to get some cards printed to get 'out there' while I design my website.

Hi, thanks for all your designs. Can you find a way to include the therapies that I offer within the card, either on the front or back…the therapies I offer are: aromatherapy massage, reflexology, swedish body massage, abdominal-sacral massage, nutrition, soul healing, aura readings. (Maybe have them with a bullet point before each?) I am not sure whether they should be on the front of the card or the back or whether having them would spoil the card but it occurred to me that just having rosa pell therapies doesn't tell people what therapies I offer, hence the new idea to list them somehow…)

Target Market(s)

Mainly women (middle class probably with disposable incomes).

Industry/Entity Type

Massage

Contact Information for Business Card

Rosa Pell Therapies, Tel: 07700 900482, email: lumacrest@postvane.com, (on back of card I want: Rosalind Pell BScHons, CPWRA, RGPC.)

Requirements
Nice to have
• A logo for Rosa Pell Therapies would be good.

```html
<!DOCTYPE html>
<html lang="en">
<head>
<meta charset="utf-8">
<title>Rosa Pell Therapies – Business Card Concepts</title>
<link rel="stylesheet" href="https://fonts.googleapis.com/css2?family=Arimo&family=EB+Garamond:wght@600;700&family=Questrial&display=swap">
<style>
  :root {
    --sheet: #ffffff;
    --sheet-edge: #e3e3e3;
    --panel: #ebebeb;
    --ink: #222222;
    --label: #333333;
    --green: #3cb34a;
    --green-light: #8fd43c;
    --green-dark: #1f9d45;
    --purple: #b87fb8;
    --purple-dark: #a56aa8;
    --white: #ffffff;
    --rule: #555555;
  }
  * { box-sizing: border-box; margin: 0; padding: 0; }
  html, body { width: 1200px; height: 620px; overflow: hidden; background: var(--sheet); }
  body { position: relative; font-family: "Arimo", Arial, sans-serif; color: var(--label); }
  .sheet { position: absolute; inset: 0; border: 1px solid var(--sheet-edge); }
  .panel { position: absolute; background: var(--panel); }
  .panel--one { left: 62px; top: 22px; width: 436px; height: 518px; }
  .panel--two { left: 548px; top: 22px; width: 437px; height: 527px; }
  .heading { position: absolute; font-size: 18px; transform: translateX(-50%); white-space: nowrap; }
  .row-num { position: absolute; font-size: 15px; }
  .card {
    position: absolute; border-radius: 14px; overflow: hidden; background: var(--white);
    box-shadow: 3px 4px 6px rgba(0,0,0,.35);
  }
  .card svg.wave { position: absolute; inset: 0; width: 100%; height: 100%; }
  .wordmark {
    position: absolute; font-family: "EB Garamond", Garamond, serif; font-weight: 700;
    color: var(--green); line-height: 1; white-space: nowrap;
  }
  .mark-dot { position: absolute; border-radius: 50%; background: var(--purple); }
  .contact {
    position: absolute; font-family: "EB Garamond", Garamond, serif; font-weight: 700;
    font-size: 14px; line-height: 21px; white-space: nowrap;
    display: flex; flex-direction: column; align-items: flex-end;
  }
  .contact--center { align-items: center; }
  .contact--light { color: var(--white); }
  .contact--dark { color: var(--ink); }
  .contact span { display: flex; align-items: center; gap: 4px; }
  .contact svg { width: 15px; height: 13px; flex: none; }
  .creds { position: absolute; font-family: "EB Garamond", Garamond, serif; font-weight: 700; font-size: 12px; color: var(--ink); white-space: nowrap; }
  .creds--sans { font-family: "Questrial", "Century Gothic", sans-serif; font-weight: 400; font-size: 14px; color: #333; }
  .card--back { background: radial-gradient(ellipse at 50% 40%, #f6eaf6 0%, #d9b0d9 55%, var(--purple) 100%); }
  .card--back .decor { position: absolute; border-radius: 50%; background: rgba(255,255,255,.35); }
  .appt-label { position: absolute; font-family: "EB Garamond", Garamond, serif; font-size: 13px; color: var(--ink); }
  .appt-line { position: absolute; left: 60px; width: 244px; height: 1px; background: var(--rule); }
  .logo-heading { position: absolute; left: 1093px; top: 16px; font-size: 16px; transform: translateX(-50%); }
  .logo-option { position: absolute; left: 1022px; width: 116px; display: flex; align-items: center; gap: 6px; }
  .logo-option .mark-dot { position: static; width: 18px; height: 18px; flex: none; }
  .logo-option .wordmark { position: static; font-size: 13px; white-space: normal; line-height: 1.1; }
</style>
</head>
<body>
<div class="sheet"></div>

<div class="panel panel--one"></div>
<div class="panel panel--two"></div>
<div class="heading" style="left:293px;top:30px;">one-sided</div>
<div class="heading" style="left:793px;top:30px;">double-sided</div>

<div class="row-num" style="left:73px;top:150px;">1</div>
<div class="row-num" style="left:73px;top:392px;">2</div>
<div class="row-num" style="left:560px;top:150px;">1</div>
<div class="row-num" style="left:560px;top:392px;">2</div>

<!-- One-sided, option 1 -->
<div class="card" style="left:100px;top:64px;width:366px;height:204px;">
  <svg class="wave" viewBox="0 0 366 204" preserveAspectRatio="none" aria-hidden="true">
    <defs>
      <linearGradient id="g1" x1="0" x2="1" y1="0" y2="0">
        <stop offset="0" stop-color="var(--green-light)"/><stop offset="1" stop-color="var(--green-dark)"/>
      </linearGradient>
    </defs>
    <path d="M0,138 C90,158 180,110 260,90 C310,78 345,76 366,76 L366,204 L0,204 Z" fill="var(--purple)"/>
    <path d="M0,144 C90,163 180,116 260,96 C310,84 345,82 366,82 L366,204 L0,204 Z" fill="var(--white)"/>
    <path d="M0,150 C90,168 180,122 260,102 C310,90 345,88 366,88 L366,204 L0,204 Z" fill="url(#g1)"/>
  </svg>
  <div class="mark-dot" style="left:58px;top:30px;width:40px;height:40px;"></div>
  <div class="wordmark" style="left:110px;top:30px;font-size:25px;">Rosa Pell<br>Therapies</div>
  <div class="contact contact--light" style="right:32px;top:122px;">
    <span><svg viewBox="0 0 15 13"><circle cx="7" cy="6.5" r="6" fill="none" stroke="currentColor"/><path d="M5 3.5 L6.5 5 L5.8 6 Q6.8 8 8 8.6 L9 7.8 L10.5 9.3 L9.5 10.3 Q6 9.5 4 5 Z" fill="currentColor"/></svg>07700 900482</span>
    <span><svg viewBox="0 0 15 13"><rect x="1" y="2" width="13" height="9" fill="none" stroke="currentColor"/><path d="M1 2 L7.5 7 L14 2" fill="none" stroke="currentColor"/></svg>lumacrest@postvane.com</span>
  </div>
  <div class="creds" style="right:32px;top:176px;">Rosalind Pell BScHons, CPWRA, RGPC.</div>
</div>

<!-- One-sided, option 2 -->
<div class="card" style="left:102px;top:305px;width:366px;height:203px;">
  <svg class="wave" viewBox="0 0 366 203" preserveAspectRatio="none" aria-hidden="true">
    <defs>
      <radialGradient id="p1" cx="0.45" cy="0.2" r="0.9">
        <stop offset="0" stop-color="#f8eef8"/><stop offset="0.5" stop-color="#d4a6d4"/><stop offset="1" stop-color="var(--purple-dark)"/>
      </radialGradient>
    </defs>
    <path d="M0,150 C100,160 190,110 270,95 C320,86 350,88 366,90 L366,203 L0,203 Z" fill="var(--green)"/>
    <path d="M0,155 C100,164 190,115 270,101 C320,92 350,94 366,96 L366,203 L0,203 Z" fill="var(--white)"/>
    <path d="M0,160 C100,168 190,120 270,107 C320,98 350,100 366,102 L366,203 L0,203 Z" fill="url(#p1)"/>
  </svg>
  <div class="mark-dot" style="left:52px;top:22px;width:40px;height:40px;"></div>
  <div class="wordmark" style="left:14px;top:76px;font-size:24px;">Rosa Pell<br>Therapies</div>
  <div class="contact contact--dark" style="right:12px;top:32px;">
    <span><svg viewBox="0 0 15 13"><circle cx="7" cy="6.5" r="6" fill="none" stroke="currentColor"/><path d="M5 3.5 L6.5 5 L5.8 6 Q6.8 8 8 8.6 L9 7.8 L10.5 9.3 L9.5 10.3 Q6 9.5 4 5 Z" fill="currentColor"/></svg>07700 900482</span>
    <span><svg viewBox="0 0 15 13"><rect x="1" y="2" width="13" height="9" fill="none" stroke="currentColor"/><path d="M1 2 L7.5 7 L14 2" fill="none" stroke="currentColor"/></svg>lumacrest@postvane.com</span>
  </div>
  <div class="creds creds--sans" style="right:22px;top:166px;">Rosalind Pell BScHons, CPWRA, RGPC.</div>
</div>

<!-- Double-sided, front -->
<div class="card" style="left:587px;top:64px;width:365px;height:220px;">
  <svg class="wave" viewBox="0 0 365 220" preserveAspectRatio="none" aria-hidden="true">
    <defs>
      <linearGradient id="g2" x1="0" x2="0" y1="0" y2="1">
        <stop offset="0" stop-color="var(--green)"/><stop offset="1" stop-color="var(--green-dark)"/>
      </linearGradient>
    </defs>
    <path d="M0,132 C60,150 110,160 180,150 C260,138 320,130 365,148 L365,220 L0,220 Z" fill="var(--purple)"/>
    <path d="M0,140 C60,156 110,164 180,154 C260,142 320,136 365,152 L365,220 L0,220 Z" fill="var(--white)"/>
    <path d="M0,148 C60,162 110,170 180,160 C260,148 320,142 365,158 L365,220 L0,220 Z" fill="url(#g2)"/>
  </svg>
  <div class="mark-dot" style="left:68px;top:40px;width:40px;height:40px;"></div>
  <div class="wordmark" style="left:122px;top:46px;font-size:25px;">Rosa Pell<br>Therapies</div>
  <div class="contact contact--dark contact--center" style="left:0;width:100%;top:166px;font-size:13px;line-height:20px;">
    <span><svg viewBox="0 0 15 13"><circle cx="7" cy="6.5" r="6" fill="none" stroke="currentColor"/><path d="M5 3.5 L6.5 5 L5.8 6 Q6.8 8 8 8.6 L9 7.8 L10.5 9.3 L9.5 10.3 Q6 9.5 4 5 Z" fill="currentColor"/></svg>07700 900482</span>
    <span><svg viewBox="0 0 15 13"><rect x="1" y="2" width="13" height="9" fill="none" stroke="currentColor"/><path d="M1 2 L7.5 7 L14 2" fill="none" stroke="currentColor"/></svg>lumacrest@postvane.com</span>
  </div>
</div>

<!-- Double-sided, back -->
<div class="card card--back" style="left:588px;top:311px;width:366px;height:212px;">
  <div class="decor" role="img" aria-label="Faint large soft-petal decoration" style="left:10px;top:30px;width:150px;height:170px;"></div>
  <div class="decor" role="img" aria-label="Faint small soft-petal decoration" style="left:285px;top:10px;width:70px;height:80px;"></div>
  <div class="creds" style="left:0;width:100%;text-align:center;top:36px;">Rosalind Pell BScHons, CPWRA, RGPC.</div>
  <div class="appt-label" style="left:143px;top:84px;">Appointment:</div>
  <div class="appt-line" style="top:121px;"></div>
  <div class="appt-line" style="top:148px;"></div>
  <div class="appt-line" style="top:175px;"></div>
</div>

<!-- Logo options -->
<div class="logo-heading">Logo</div>
<div class="logo-option" style="top:90px;"><div class="mark-dot"></div><div class="wordmark">Rosa Pell Therapies</div></div>
<div class="logo-option" style="top:200px;"><div class="mark-dot" style="background:var(--green);"></div><div class="wordmark">Rosa Pell Therapies</div></div>
<div class="logo-option" style="top:308px;"><div class="mark-dot"></div><div class="wordmark">Rosa Pell Therapies</div></div>
<div class="logo-option" style="top:417px;"><div class="mark-dot" style="background:var(--green);"></div><div class="wordmark">Rosa Pell Therapies</div></div>
<div class="row-num" style="left:1156px;top:92px;">1</div>
<div class="row-num" style="left:1156px;top:202px;">2</div>
<div class="row-num" style="left:1156px;top:310px;">3</div>
<div class="row-num" style="left:1156px;top:419px;">4</div>
</body>
</html>
```